Etiketten-Design für neue Biermarke
Zielgruppe
Es soll eine neue Biermarke entwickelt werden. Die drei grundlegenden Sorten sind: Pils, Radler, Helles. Für die neue Biermarke soll ein Markenname, ein Logo und ein Etikettendesign gestaltet werden. Das Bier soll traditionell sein und den typischen Biertrinker ansprechen. Die Zielgruppe der Biermarke ist die breite Masse. Das Bier soll für 9,90€ verkauft werden.
Aufgabenstellung
Das Design der Etiketten sollte klassisch und traditionell wirken. Es dürfen gerne klassische, historische und urige Elemente wie Hopfen, Bierfass, altertümliche Illustrationen, etc. verwendet werden. Das Bier sollte weder in Richtung eines Craft Bieres noch in die Richtung eines jungen/hippen Bieres gehen.

```html
<!DOCTYPE html>
<html lang="de">
<head>
<meta charset="utf-8">
<title>Alt-Holzner Pilsner – Etikett Helles</title>
<link rel="stylesheet" href="https://fonts.googleapis.com/css2?family=Abril+Fatface&family=Playfair+Display:wght@700&family=Yellowtail&display=swap">
<style>
  :root {
    --paper: #ffffff;
    --gold-dark: #a08c5a;
    --gold-light: #d6c594;
    --brown: #33150c;
    --brown-soft: #4a2418;
    --hop-gold: #b8945a;
    --ribbon: #a62825;
    --ribbon-shade: #8e1f1d;
    --ribbon-fold: #6a1412;
  }
  html, body {
    margin: 0;
    padding: 0;
    width: 1051px;
    height: 1200px;
    overflow: hidden;
    background: var(--paper);
  }
  .label {
    display: block;
    width: 1051px;
    height: 1200px;
  }
  .ring-text {
    font-family: "Playfair Display", serif;
    font-weight: 700;
    font-size: 15px;
    fill: var(--brown);
  }
  .year {
    font-family: "Abril Fatface", serif;
    font-size: 72px;
    fill: var(--brown);
  }
  .brand-name {
    font-family: "Abril Fatface", serif;
    font-size: 178px;
    fill: var(--brown);
  }
  .variety {
    font-family: "Abril Fatface", serif;
    font-size: 112px;
    fill: var(--brown);
  }
  .ribbon-title {
    font-family: "Yellowtail", cursive;
    font-size: 84px;
    fill: var(--paper);
  }
</style>
</head>
<body>
<svg class="label" viewBox="0 0 1051 1200" xmlns="http://www.w3.org/2000/svg">
  <defs>
    <linearGradient id="goldSheen" x1="0" y1="0" x2="1" y2="0">
      <stop offset="0" stop-color="var(--gold-dark)"/>
      <stop offset="0.5" stop-color="var(--gold-light)"/>
      <stop offset="1" stop-color="var(--gold-dark)"/>
    </linearGradient>
    <path id="ringPath" d="M140,608 A382,474 0 1,1 904,608 A382,474 0 1,1 140,608"/>
    <path id="varietyArc" d="M330,918 Q522,1045 716,904"/>
  </defs>

  <!-- Oval frame -->
  <g class="frame">
    <ellipse cx="522" cy="608" rx="463" ry="578" fill="url(#goldSheen)"/>
    <ellipse cx="522" cy="608" rx="446" ry="546" fill="var(--paper)"/>
    <ellipse cx="522" cy="608" rx="440" ry="538" fill="none" stroke="url(#goldSheen)" stroke-width="3"/>
  </g>

  <!-- Circular claim -->
  <text class="ring-text" text-anchor="middle" letter-spacing="4.5">
    <textPath href="#ringPath" startOffset="25%">NACH DEUTSCHER BRAUQUALITÄT · PREMIUM PILS · GARANTIERT BESTE ROHSTOFFE</textPath>
  </text>
  <text class="ring-text" text-anchor="middle" letter-spacing="4.5">
    <textPath href="#ringPath" startOffset="75%">NACH DEUTSCHER BRAUQUALITÄT · PREMIUM PILS · GARANTIERT BESTE ROHSTOFFE</textPath>
  </text>

  <!-- Ribbon with variety -->
  <g class="ribbon">
    <path d="M282,302 L322,296 L360,387 Q322,391 286,400 Q283,388 292,372 L304,340 Z" fill="var(--ribbon-shade)"/>
    <path d="M769,302 L729,296 L691,387 Q729,391 765,400 Q768,388 759,372 L747,340 Z" fill="var(--ribbon-shade)"/>
    <path d="M336,365 L360,387 L358,368 Z" fill="var(--ribbon-fold)"/>
    <path d="M708,365 L691,387 L693,368 Z" fill="var(--ribbon-fold)"/>
    <path d="M320,271 Q522,242 723,271 L708,365 Q522,340 336,365 Z" fill="var(--ribbon)"/>
    <text class="ribbon-title" x="526" y="334" text-anchor="middle">Helles</text>
  </g>

  <!-- Crest illustration: two lions holding a tapped barrel -->
  <rect class="crest-illustration" role="img" aria-label="Illustration: zwei aufgerichtete Löwen halten ein Bierfass mit Zapfhahn"
        x="328" y="394" width="392" height="188" rx="40" fill="var(--brown-soft)"/>

  <!-- Founding year -->
  <text class="year" x="154" y="563" text-anchor="middle">18</text>
  <text class="year" x="886" y="563" text-anchor="middle">97</text>

  <!-- Brand name -->
  <text class="brand-name" x="534" y="730" text-anchor="middle" textLength="682" lengthAdjust="spacingAndGlyphs">ALT-HOLZNER</text>

  <!-- Hop cones -->
  <rect class="hops-illustration" role="img" aria-label="Illustration: drei Hopfendolden"
        x="415" y="777" width="202" height="98" rx="30" fill="var(--hop-gold)" opacity="0.85"/>

  <!-- Beer style -->
  <text class="variety" text-anchor="middle">
    <textPath href="#varietyArc" startOffset="50%" textLength="390" lengthAdjust="spacingAndGlyphs">PILSNER</textPath>
  </text>
</svg>
</body>
</html>
```